Flyer für Lettershop
Zielgruppe
Informationen entnehmen Sie bitte: http://www.postfunk-versand.example
Aufgabenstellung
Entwurf eines 6-Seiter Flyer. Dieser soll später als Selfmailer verschickt werden.
Eine grobe Vorstellung entnehmen Sie bitte dem Anhang. Dies soll nur eine kleine Inspiration sein, Sie müssen sich nicht an diese Vorlage halten.
Drei Hauptprodukte bieten wir an: Kuvertierte Mailings (Formate: DIN-L, C5, C4 - Maschine Travolin KX-4700), Postkarten und Selfmailer. Wir möchten das die Preise ins Auge fallen, trotsdem bieten wir eine perfekte und professionelle Qualität.
Informationen und Bilder können Sie postfunk-versand.example entnehmen.
Texte auf Wunsch auch von unserem Subunternehmen: http://www.briefwerk-satz.example/about-us/
Sollten Sie Fragen oder Wünsche haben, zögern Sie bitte nicht uns zu kontaktieren.

```html
<!DOCTYPE html>
<html lang="de">
<head>
<meta charset="utf-8">
<title>Lettershop Flyer – Top-Angebote</title>
<link rel="stylesheet" href="https://fonts.googleapis.com/css2?family=Ubuntu:wght@400;500;700&display=swap">
<style>
  :root {
    --orange: #f7931e;
    --orange-light: #fba21f;
    --dark: #3b3b3b;
    --text: #333333;
    --list: #4a3f35;
    --white: #ffffff;
    --stage: #e9e7e4;
    --photo-a: #d9d7d2;
    --photo-b: #6d6a66;
  }
  * { box-sizing: border-box; margin: 0; padding: 0; }
  html, body { width: 1200px; height: 900px; overflow: hidden; }
  body { background: var(--stage); font-family: "Ubuntu", sans-serif; position: relative; }

  .flyer {
    position: absolute; left: 42px; top: 68px;
    width: 1113px; height: 759px;
    background: var(--white);
    box-shadow: 0 4px 14px rgba(0,0,0,.25);
    overflow: hidden;
  }
  .flyer__shapes { position: absolute; inset: 0; }
  .block { position: absolute; }

  .intro__headline {
    left: 36px; top: 40px; width: 320px;
    color: var(--white); font-weight: 700; font-size: 24.5px; line-height: 34px;
  }
  .intro__body {
    left: 36px; top: 246px; width: 300px;
    color: var(--text); font-size: 11.6px; line-height: 16.6px;
    hyphens: auto;
  }
  .intro__body p { margin-bottom: 16.6px; }
  .intro__refs-title {
    left: 36px; top: 536px; width: 300px;
    color: var(--orange); font-weight: 700; font-size: 20px; line-height: 27px;
  }
  .intro__refs-body {
    left: 36px; top: 608px; width: 305px;
    color: var(--text); font-size: 11.6px; line-height: 16.6px; hyphens: auto;
  }

  .offers__title {
    left: 373px; top: 40px; width: 375px; text-align: center;
    color: var(--orange); font-weight: 700; font-size: 24px;
  }

  .offer__name { font-weight: 700; font-size: 23px; line-height: 30px; }
  .offer__sub { font-weight: 700; font-size: 14.5px; line-height: 20px; color: var(--dark); margin-bottom: 18px; }
  .offer__list { list-style: none; font-size: 13.6px; line-height: 23px; color: var(--list); }
  .offer__list li { padding-left: 9px; text-indent: -9px; }
  .offer__list li::before { content: "- "; }
  .offer__list .wrap { line-height: 19px; margin-bottom: 4px; }
  .offer__sample { font-weight: 700; font-size: 13.6px; color: var(--dark); margin-top: 12px; }

  .offer--one { left: 411px; top: 426px; width: 330px; }
  .offer--one .offer__name { color: var(--white); }
  .offer--one .offer__list li { margin-bottom: 0; }

  .offer--two { left: 787px; top: 40px; width: 290px; }
  .offer--two .offer__name { color: var(--white); }
  .offer--two .offer__sub { margin-bottom: 12px; }
  .offer--two .offer__list { font-size: 13.2px; }

  .offer--three { left: 793px; top: 364px; width: 305px; }
  .offer--three .offer__name { color: var(--orange); }
  .offer--three .offer__sub { margin-bottom: 12px; }
  .offer--three .offer__list { font-size: 13.2px; }

  .price {
    position: absolute; width: 140px; height: 140px; border-radius: 50%;
    background: var(--dark); color: var(--white);
    display: flex; align-items: center; justify-content: center; text-align: center;
    font-weight: 700; font-size: 13px; line-height: 18px;
  }
  .price--one { left: 608px; top: 636px; }
  .price--two { left: 949px; top: 222px; }
  .price--three { left: 949px; top: 575px; }
</style>
</head>
<body>
<div class="flyer">
  <svg class="flyer__shapes" width="1113" height="759" viewBox="0 0 1113 759">
    <defs>
      <linearGradient id="machinePhoto" x1="0" y1="0" x2="1" y2="1">
        <stop offset="0" stop-color="var(--photo-a)"/>
        <stop offset="1" stop-color="var(--photo-b)"/>
      </linearGradient>
      <linearGradient id="stackPhoto" x1="0" y1="0" x2="1" y2="0">
        <stop offset="0" stop-color="#c9cfd3"/>
        <stop offset="1" stop-color="#8e959a"/>
      </linearGradient>
    </defs>
    <!-- panel 1 -->
    <polygon points="0,0 373,0 373,147 0,202" fill="var(--orange)"/>
    <polygon points="0,213 373,158 373,171 0,227" fill="var(--dark)"/>
    <!-- panel 2 -->
    <rect x="373" y="0" width="375" height="400" fill="var(--dark)"/>
    <polygon points="373,150 748,92 748,335 373,380" fill="url(#machinePhoto)" role="img" aria-label="Foto: Kuvertiermaschine im Lettershop"/>
    <polygon points="373,393 748,347 748,759 373,759" fill="var(--orange)"/>
    <!-- panel 3 -->
    <polygon points="748,0 1113,0 1113,276 748,333" fill="var(--orange)"/>
    <polygon points="748,341 1113,284 1113,296 748,353" fill="var(--dark)"/>
    <polygon points="748,646 1113,597 1113,759 748,759" fill="url(#stackPhoto)" role="img" aria-label="Foto: gestapelte Selfmailer"/>
  </svg>

  <h1 class="block intro__headline">Wir bieten unseren Kunden den kompletten Lettershop Service ...</h1>
  <div class="block intro__body">
    <p>... mit all seinen Facetten an, vom Laserauftrag bis zur Portooptimierten Postauflieferung.</p>
    <p>Sprechen Sie uns an, wenn Sie eine Werbeaussendung oder ein Mailing planen. Publikationen einmalig oder regelmäßig versenden wollen oder anderweitig den direkten Weg zu Ihren Kunden suchen und hierfür fachliches Know-how benötigen.</p>
    <p>Die individuelle Beratung, die persönliche Betreuung und die kompetente Realisierung Ihrer Wünsche sind bei uns in besten Händen, zuverlässig und kostenoptimiert.Kurzfristig abzuwickelnde Großaufträge oder kleine Auflagen zwischendurch, wir stehen unseren Kunden mit unsere Lettershop-Erfahrung gleichberechtigt und immer vollumfänglich zur Verfügung.</p>
  </div>
  <h2 class="block intro__refs-title">Unsere Referenzen sind erstklassig.</h2>
  <p class="block intro__refs-body">Unternehmen aus ganz unterschiedlichen Bereichen greifen immer wieder zufrieden auf unsere Mitarbeit zurück. Für uns das sichere Zeichen, dass unsere Leistung, unser Know-how und unsere Fachkompetenz Anerkennung finden.</p>

  <h2 class="block offers__title">Unsere Top-Angebote</h2>

  <section class="block offer offer--one">
    <h3 class="offer__name">Angebot 1</h3>
    <p class="offer__sub">Briefmailing DIN-L Auflage 5.000 Stück</p>
    <ul class="offer__list">
      <li>Datenübernahme</li>
      <li>Druck A4 Briefbogen 4/0-farbig 90 gm²</li>
      <li>Druck A4 Flyer 4/4-farbig 135 gm²</li>
      <li>Personalisieren &amp; Text- Lasern schwarz/1-seitig</li>
      <li>Briefhüllen C6/5 mit Fenster ohne Druck</li>
      <li>Falzen</li>
      <li>Kuvertieren 2 Teile maschinell</li>
      <li>Postaufliefern</li>
    </ul>
    <p class="offer__sample">Muster: Brief, Flyer, Hülle</p>
  </section>

  <section class="block offer offer--two">
    <h3 class="offer__name">Angebot 2</h3>
    <p class="offer__sub">Kartenmailing Auflage 5.000 Stück</p>
    <ul class="offer__list">
      <li>Datenübernahme</li>
      <li class="wrap">Druck Maxi Postkarte 260 g/m² (23,5 cm x 12,5 cm mit Hochglanz-UV-Lack auf der Vorderseite)</li>
      <li class="wrap">Inkjet-Adressieren auf Rückseite (1/0-farbig schwarz)</li>
      <li>Postaufliefern</li>
    </ul>
    <p class="offer__sample">Muster: MaxiKarte</p>
  </section>

  <section class="block offer offer--three">
    <h3 class="offer__name">Angebot 3</h3>
    <p class="offer__sub">Selfmailer Auflage 5.000 Stück</p>
    <ul class="offer__list">
      <li>Datenübernahme</li>
      <li class="wrap">Druck Selfmailer 170 g/m² matt A4 gefalzt auf DIN lang, 6-seiter (Wickelfalz)</li>
      <li class="wrap">4/4-farbig, mit zwei transparente, perforierte Klebepunkte verschließen</li>
      <li>Inkjet-Adressieren 1-Seitig schwarz</li>
      <li>Postaufliefern</li>
    </ul>
    <p class="offer__sample">Muster: Selfmailer</p>
  </section>

  <div class="price price--one">5.000 Stück<br>Nur 495,-- €<br>zzgl. MwSt.<br>+ Porto</div>
  <div class="price price--two">5.000 Stück<br>Nur 295,-- €<br>zzgl. MwSt.<br>+ Porto</div>
  <div class="price price--three">5.000 Stück<br>Nur 495,-- €<br>zzgl. MwSt.<br>+ Porto</div>
</div>
</body>
</html>
```